Brightway Haul & Repair Services, are a company that offers a 'one stop shop' pre-move clean up a

I have already selected a logo which I would like on the front of the business cards along with phone numbers, web address and email which are:
0419574302
www.brightwayhaul.com.au
brightwayhaulrepair@mailbox.example

On the back of the card I would like to list some of the types of service we offer (clean - move - repairs/maintenance) which are:
CLEAN - windows, gutters, solar panels, driveways/paths, carpets.
MOVE - Small/medium size house/office moves, large item pick-up & delivery, yard clean-up and removal.
General maintenance and repairs.

I would like the blue logo on a gray background.

Thanks

```html
<!DOCTYPE html>
<html lang="en">
<head>
<meta charset="utf-8">
<title>Brightway Haul &amp; Repair Services – Services Card</title>
<link rel="stylesheet" href="https://fonts.googleapis.com/css2?family=Questrial&display=swap">
<style>
  :root {
    --page-bg: #ffffff;
    --card-edge: #1d67b5;
    --card-mid: #3f8bd6;
    --card-glow: #78b6ea;
    --overlay-grey: #9b9b9b;
    --ink-light: #ffffff;
    --icon-dark: #2f3438;
  }
  html, body {
    margin: 0;
    padding: 0;
    width: 1200px;
    height: 927px;
    overflow: hidden;
    background: var(--page-bg);
  }
  .canvas {
    position: relative;
    width: 1200px;
    height: 927px;
    font-family: "Questrial", "Century Gothic", sans-serif;
  }
  .service-card {
    position: absolute;
    left: 36px;
    top: 189px;
    width: 984px;
    height: 561px;
    border-radius: 45px;
    overflow: hidden;
    background: radial-gradient(ellipse 60% 70% at 28% 32%, var(--card-glow) 0%, var(--card-mid) 45%, var(--card-edge) 100%);
  }
  .card-arcs {
    position: absolute;
    inset: 0;
    width: 100%;
    height: 100%;
  }
  .card-arcs circle {
    fill: var(--overlay-grey);
    opacity: 0.5;
  }
  .card-text {
    position: absolute;
    margin: 0;
    color: var(--ink-light);
    line-height: 1;
    white-space: nowrap;
  }
  .section-title {
    font-size: 30px;
    letter-spacing: 0.5px;
  }
  .service-list {
    list-style: none;
    padding: 0;
    font-size: 33px;
  }
  .service-list li {
    height: 43px;
  }
  .title-clean { left: 94px; top: 274px; }
  .list-clean { left: 235px; top: 314px; }
  .title-move { left: 94px; top: 442px; }
  .list-move { left: 216px; top: 482px; }
  .list-move li.yard { margin-left: -3px; }
  .general-line { left: 94px; top: 650px; font-size: 33px; }
  .icon-slot {
    position: absolute;
    border-radius: 8px;
    background: linear-gradient(135deg, #3b4247, var(--icon-dark));
    opacity: 0.85;
  }
  .icon-clean { left: 90px; top: 312px; width: 102px; height: 81px; }
  .icon-move { left: 102px; top: 483px; width: 103px; height: 84px; }
  .icon-repair { left: 691px; top: 642px; width: 56px; height: 54px; border-radius: 50%; }
</style>
</head>
<body>
<main class="canvas">
  <section class="service-card" aria-label="Services offered">
    <svg class="card-arcs" viewBox="0 0 656 374" preserveAspectRatio="none" aria-hidden="true">
      <circle cx="576" cy="-106" r="380"/>
      <circle cx="640" cy="70" r="250"/>
      <circle cx="690" cy="210" r="200"/>
    </svg>
  </section>

  <h2 class="card-text section-title title-clean">CLEAN</h2>
  <div class="icon-slot icon-clean" role="img" aria-label="Cleaning brush and dustpan illustration"></div>
  <ul class="card-text service-list list-clean">
    <li>Windows, gutters, solar panels</li>
    <li>Driveways/paths, carpets.</li>
  </ul>

  <h2 class="card-text section-title title-move">MOVE</h2>
  <div class="icon-slot icon-move" role="img" aria-label="Figure pushing a load illustration"></div>
  <ul class="card-text service-list list-move">
    <li>Small/medium size house/office moves</li>
    <li>Large item pick-up &amp; delivery</li>
    <li class="yard">Yard clean-up and removal.</li>
  </ul>

  <p class="card-text general-line">General maintenance and repairs.</p>
  <div class="icon-slot icon-repair" role="img" aria-label="Maintenance symbol"></div>
</main>
</body>
</html>
```